Business Card for Modern Marketing Consultancy

Business card needed for marketing consultancy with existing logo.

Lanternway Co is a specialized boutique marketing consultancy that provides startup, small and mid size consumer businesses thought leadership and implementation of marketing strategies to help your business grow.

Our expertise, experience and industry knowledge stems from some of New York’s top global beauty and retail companies and allows us to draw from an array of successful marketing strategies and growth tactics tailored to suit the needs of your business

lanternwayco.example

Target Market(s)

start up, small and mid size consumer packaged goods businesses

Industry/Entity Type

Leadership

Requirements
Must have
• Must have the logo of the business and use of the exact colors of the logo.
Must be simple, sleek, modern and clean. Must make a statement and be eye catching.

Front: looking for unique design or visual statement with logo and tagline

Back of card should have:
logo - if not use on front.
Delia R. Horvath
Founder
Lanternway Co
m: 555.014.2276
deliahorvath@lanternwayco.example
lanternwayco.example

Please use the following words as these describe my services:
strategy analytics branding research

Please refer to the website look and feel: lanternwayco.example

Please kindly note that I am looking for a unique design that I cannot do myself with a template. thank you.
Nice to have
• Please also try and incorporate additional files attached.

```html
<!DOCTYPE html>
<html lang="en">
<head>
<meta charset="utf-8">
<title>Lanternway Co — Business Card</title>
<link rel="stylesheet" href="https://fonts.googleapis.com/css2?family=Jost:wght@300;400&display=swap">
<style>
  :root {
    --magenta: #b0155f;
    --ink-grey: #6b6b6b;
    --soft-grey: #8a8a8a;
    --card: #ededed;
    --backdrop: #d9d6d2;
  }
  * { margin: 0; padding: 0; box-sizing: border-box; }
  html, body {
    width: 1200px;
    height: 900px;
    overflow: hidden;
    background: var(--backdrop);
    font-family: "Jost", "Futura", sans-serif;
  }
  .stage {
    position: relative;
    width: 1200px;
    height: 900px;
  }
  .card {
    position: absolute;
    left: 320px;
    width: 560px;
    height: 320px;
    background: var(--card);
    box-shadow: 0 2px 0 #dcdcdc, 0 4px 0 #d2d2d2, 0 10px 24px rgba(0,0,0,0.18);
  }
  .card--front { top: 100px; }
  .card--back  { top: 480px; }

  /* Front */
  .front__name {
    position: absolute;
    left: 44px;
    top: 96px;
    font-size: 58px;
    font-weight: 400;
    color: var(--ink-grey);
    letter-spacing: 0.5px;
  }
  .front__tagline {
    position: absolute;
    left: 124px;
    top: 166px;
    font-size: 17px;
    font-weight: 400;
    color: var(--magenta);
    letter-spacing: 1.5px;
  }
  .front__rule {
    position: absolute;
    left: 290px;
    right: 0;
    top: 212px;
    height: 1.5px;
    background: var(--magenta);
  }
  .front__services {
    position: absolute;
    right: 28px;
    top: 222px;
    font-size: 14px;
    font-weight: 300;
    color: var(--soft-grey);
    letter-spacing: 0.5px;
  }

  /* Back */
  .back__brand {
    position: absolute;
    right: 40px;
    top: 40px;
    display: flex;
    align-items: center;
    gap: 10px;
    font-size: 26px;
    font-weight: 400;
    color: var(--magenta);
  }
  .back__brand-dot {
    width: 22px;
    height: 22px;
    border-radius: 50%;
    background: var(--magenta);
  }
  .contact {
    position: absolute;
    left: 40px;
    top: 118px;
  }
  .contact__label {
    font-size: 22px;
    font-weight: 300;
    color: var(--magenta);
    letter-spacing: 1px;
  }
  .contact__name {
    font-size: 20px;
    font-weight: 300;
    color: var(--ink-grey);
    letter-spacing: 0.5px;
    margin-top: 2px;
  }
  .contact__role {
    font-size: 14px;
    font-weight: 300;
    color: var(--soft-grey);
  }
  .contact__lines {
    margin-top: 14px;
    font-size: 14px;
    font-weight: 300;
    color: var(--soft-grey);
    line-height: 1.3;
  }
  .contact__key {
    display: inline-block;
    width: 16px;
    color: var(--magenta);
  }
  .back__rule {
    position: absolute;
    left: 0;
    width: 290px;
    top: 262px;
    height: 1.5px;
    background: var(--magenta);
  }
  .back__web {
    position: absolute;
    left: 40px;
    top: 274px;
    font-size: 15px;
    font-weight: 300;
    color: var(--ink-grey);
  }
</style>
</head>
<body>
<main class="stage">
  <section class="card card--front" aria-label="Card front">
    <div class="front__name">Lanternway Co</div>
    <div class="front__tagline">discover | intelligent marketing</div>
    <div class="front__rule"></div>
    <div class="front__services">strategy | analytics | branding | research</div>
  </section>

  <section class="card card--back" aria-label="Card back">
    <div class="back__brand"><span class="back__brand-dot"></span>Lanternway Co</div>
    <div class="contact">
      <div class="contact__label">CONTACT:</div>
      <div class="contact__name">DELIA R. HORVATH</div>
      <div class="contact__role">Founder</div>
      <div class="contact__lines">
        <div><span class="contact__key">M</span>555.014.2276</div>
        <div><span class="contact__key">E</span>deliahorvath@lanternwayco.example</div>
      </div>
    </div>
    <div class="back__rule"></div>
    <div class="back__web">lanternwayco.example</div>
  </section>
</main>
</body>
</html>
```